Cover Art Needed For Digital Single Release

We are looking to have the cover art designed for a new song called "Paper Lanterns". You will find the track attached below in a private TuneVault link so that you can have a listen.
We are thinking of keeping the artwork fairly simple but still want it to catch your eye. Maybe using the song title and artist’s name in a colorful and creative way. (A well-designed font with a bold color scheme, or even something like a mosaic style art piece featuring the title).
We completely welcome any and all creative visions you might have, even if it strays away from the examples given above.
Thank you in advance for your submissions, and we are excited to collaborate with you!
"Paper Lanterns" by Tobin Marsh
https://tunevault.example/tobinxyz/paper-lanterns/s-r7Tq2wLmNcx
Target Market(s)
Teens/Young Adults
Industry/Entity Type
Music
Requirements
Must have
- An eye-catching design
Should not have
- Please do not rely heavily on stock images. We prefer an original design/concept.

```html
<!DOCTYPE html>
<html lang="en">
<head>
<meta charset="utf-8">
<title>Paper Lanterns – Tobin Marsh</title>
<link rel="stylesheet" href="https://fonts.googleapis.com/css2?family=Titan+One&family=Montserrat:wght@600&display=swap">
<style>
  :root {
    --wall-light: #a9a5bd;
    --wall-dark: #8d89a3;
    --title-outline: #4a3a14;
    --tile-yellow: #f4d21e;
    --tile-white: #f6f4ee;
    --tile-blue: #3fb6ea;
    --tile-pink: #f07ba0;
    --tile-orange: #f4a21c;
    --tile-green: #5cc95a;
    --frame-light: #b08a5c;
    --frame-mid: #7a5630;
    --frame-dark: #3d2814;
    --plaque: #f1f7b4;
    --name-ink: #5a3e28;
  }
  html, body {
    margin: 0;
    padding: 0;
    width: 1200px;
    height: 1200px;
    overflow: hidden;
    background: var(--wall-dark);
  }
  .cover {
    display: block;
    width: 1200px;
    height: 1200px;
  }
  .title-line {
    font-family: "Titan One", sans-serif;
    font-size: 330px;
    fill: url(#mosaicTones);
    stroke: var(--title-outline);
    stroke-width: 12px;
    paint-order: stroke fill;
    stroke-linejoin: round;
  }
  .artist-name {
    font-family: "Montserrat", sans-serif;
    font-weight: 600;
    font-size: 100px;
    fill: var(--name-ink);
  }
</style>
</head>
<body>
<svg class="cover" viewBox="0 0 1200 1200" xmlns="http://www.w3.org/2000/svg">
  <defs>
    <radialGradient id="wallTone" cx="50%" cy="45%" r="75%">
      <stop offset="0" stop-color="var(--wall-light)"/>
      <stop offset="1" stop-color="var(--wall-dark)"/>
    </radialGradient>
    <linearGradient id="mosaicTones" x1="0" y1="0" x2="1" y2="1">
      <stop offset="0" stop-color="var(--tile-pink)"/>
      <stop offset="0.2" stop-color="var(--tile-yellow)"/>
      <stop offset="0.4" stop-color="var(--tile-white)"/>
      <stop offset="0.55" stop-color="var(--tile-blue)"/>
      <stop offset="0.7" stop-color="var(--tile-yellow)"/>
      <stop offset="0.85" stop-color="var(--tile-green)"/>
      <stop offset="1" stop-color="var(--tile-orange)"/>
    </linearGradient>
    <linearGradient id="frameWood" x1="0" y1="0" x2="0" y2="1">
      <stop offset="0" stop-color="var(--frame-light)"/>
      <stop offset="0.5" stop-color="var(--frame-mid)"/>
      <stop offset="1" stop-color="var(--frame-dark)"/>
    </linearGradient>
  </defs>

  <rect class="wall" width="1200" height="1200" fill="url(#wallTone)" role="img" aria-label="Grey-lavender flagstone wall background"/>

  <g class="title">
    <text class="title-line" x="600" y="334" text-anchor="middle" textLength="980" lengthAdjust="spacingAndGlyphs">PAPER</text>
    <text class="title-line" x="600" y="656" text-anchor="middle" textLength="980" lengthAdjust="spacingAndGlyphs">LANTERNS</text>
  </g>

  <g class="name-plaque">
    <rect class="frame-outer" x="114" y="702" width="972" height="438" fill="url(#frameWood)" stroke="var(--frame-dark)" stroke-width="4"/>
    <rect class="frame-bevel" x="148" y="736" width="904" height="370" fill="none" stroke="var(--frame-dark)" stroke-width="6" opacity="0.6"/>
    <rect class="frame-inner" x="182" y="782" width="836" height="284" fill="var(--frame-mid)" stroke="var(--frame-dark)" stroke-width="4"/>
    <rect class="plaque-panel" x="198" y="798" width="804" height="252" fill="var(--plaque)"/>
    <text class="artist-name" x="600" y="960" text-anchor="middle" textLength="720" lengthAdjust="spacingAndGlyphs">TOBIN MARSH</text>
  </g>
</svg>
</body>
</html>
```